New Graphic Design Project

Design a simple and clean PowerPoint slide templates for a Board meeting. The slides should have predominantly white backgrounds and use the brand graphic standards (attached). I'm also attached a PowerPoint master that I don't like, as it's too basic.
The company name is Harbor Lane Gauging.
It sells, calibrates, services and repairs industrial and commercial scales of all types. In particular, Truck scales, floor scales, counting scales and benchtop scales.
The website is harborlanegauging.example but this are the old colors, so ignore the logo and colors. We are launching a new logo and new look. Several variations of the logo are available.

```html
<!DOCTYPE html>
<html lang="en">
<head>
<meta charset="utf-8">
<title>Harbor Lane Gauging – Board Slide Templates</title>
<link rel="stylesheet" href="https://fonts.googleapis.com/css2?family=Barlow:wght@300;400;600;700&family=Barlow+Semi+Condensed:wght@700&family=Poppins:wght@300;400;500&display=swap">
<style>
  :root {
    --navy: #1b2f5c;
    --navy-deep: #16244a;
    --orange: #f7982a;
    --white: #ffffff;
    --canvas: #e2e2e2;
    --ink: #2a2f3d;
    --font-head: "Barlow Semi Condensed", "Barlow", sans-serif;
    --font-ui: "Barlow", sans-serif;
    --font-body: "Poppins", sans-serif;
  }
  * { box-sizing: border-box; margin: 0; padding: 0; }
  html, body { width: 1200px; height: 1200px; overflow: hidden; }
  body { background: var(--canvas); position: relative; font-family: var(--font-body); }

  .slide { position: absolute; overflow: hidden; background: var(--white); }
  .slide > * { position: absolute; }

  /* Cover slide */
  .cover { left: 185px; top: 70px; width: 830px; height: 467px; }
  .cover-photo { inset: 0; background: radial-gradient(ellipse at 62% 40%, #2f4270 0%, #22315a 40%, var(--navy-deep) 80%); }
  .cover-name { left: 133px; top: 138px; width: 270px; font-family: var(--font-ui); font-weight: 700; font-size: 36px; line-height: 38px; letter-spacing: 2px; color: var(--white); text-transform: uppercase; }
  .cover-rule { left: 133px; top: 226px; width: 295px; height: 1px; background: var(--orange); }
  .cover-url { left: 133px; top: 240px; font-family: var(--font-body); font-weight: 300; font-size: 11.5px; color: var(--orange); }
  .cover-url b { color: var(--white); font-weight: 400; }
  .cover-panel { left: 428px; top: 187px; width: 402px; height: 280px; background: var(--orange); }
  .cover-title { left: 464px; top: 226px; font-family: var(--font-head); font-size: 33px; line-height: 36px; color: var(--white); }
  .cover-title span { color: var(--navy); display: block; }

  /* Content slides */
  .content { width: 482px; height: 271px; }
  .s-one { left: 93px; top: 569px; }
  .s-two { left: 600px; top: 569px; }
  .s-band { left: 93px; top: 864px; }
  .s-close { left: 600px; top: 864px; }

  .subtitle { right: 372px; top: 37px; font-family: var(--font-ui); font-weight: 600; font-size: 10px; color: var(--orange); text-align: right; }
  .heading { right: 372px; top: 67px; font-family: var(--font-head); font-size: 14px; line-height: 15px; color: var(--orange); text-align: right; }
  .heading span { display: block; color: var(--navy); }
  .divider { left: 123px; top: 66px; width: 1px; height: 194px; background: var(--orange); }

  .col-head { font-family: var(--font-body); font-weight: 300; font-size: 12px; color: var(--orange); }
  .col-body { font-family: var(--font-body); font-weight: 300; font-size: 6.4px; line-height: 8.6px; color: var(--ink); }

  .footer-name { left: 21px; top: 246px; font-family: var(--font-ui); font-weight: 700; font-size: 6px; color: var(--navy); text-transform: uppercase; letter-spacing: .4px; }
  .footer-rule-accent { left: 52px; top: 258px; width: 72px; height: 2px; background: var(--orange); }
  .footer-rule { left: 124px; top: 258px; width: 341px; height: 2px; background: var(--navy); }

  .lead-box { left: 124px; top: 24px; width: 358px; height: 93px; background: var(--navy); }
  .lead-text { left: 148px; top: 72px; width: 310px; font-family: var(--font-body); font-weight: 500; font-size: 7.4px; line-height: 9.6px; color: var(--white); }

  .band-photo-warm { left: 0; top: 0; width: 124px; height: 117px; background: linear-gradient(135deg, #e99a3c, #d7862b); }
  .band-photo-cool { left: 124px; top: 0; width: 358px; height: 117px; background: linear-gradient(120deg, #2b3d66 0%, var(--navy-deep) 60%, #1c2a52 100%); }
  .band-sub { left: 148px; top: 57px; font-family: var(--font-ui); font-weight: 600; font-size: 10px; color: var(--white); }
  .band-title { left: 148px; top: 87px; font-family: var(--font-head); font-size: 14px; color: var(--white); white-space: nowrap; }
  .band-title span { color: var(--orange); }

  .close-navy { left: 251px; top: 0; width: 231px; height: 135px; background: var(--navy); }
  .close-orange { left: 163px; top: 135px; width: 88px; height: 136px; background: var(--orange); }
  .close-name { left: 76px; top: 80px; width: 165px; font-family: var(--font-ui); font-weight: 700; font-size: 20px; line-height: 21px; letter-spacing: 1px; color: var(--navy); text-transform: uppercase; }
  .close-url { left: 273px; top: 253px; font-family: var(--font-body); font-weight: 300; font-size: 6.6px; color: var(--ink); }
  .close-url span { color: var(--orange); }
</style>
</head>
<body>

<section class="slide cover">
  <div class="cover-photo" role="img" aria-label="Dark navy-toned photo of a hand adjusting a precision measuring instrument"></div>
  <div class="cover-name">Harbor Lane<br>Gauging</div>
  <div class="cover-rule"></div>
  <div class="cover-url">harborlane<b>gauging</b>.example</div>
  <div class="cover-panel"></div>
  <h1 class="cover-title">One Column<span>With Heading</span></h1>
</section>

<section class="slide content s-one">
  <div class="subtitle">SUB TITLE</div>
  <h2 class="heading">One Column<span>With Heading</span></h2>
  <div class="divider"></div>
  <div class="col-head" style="left:148px; top:66px;">Column one heading</div>
  <p class="col-body" style="left:148px; top:92px; width:300px;">Lorem ipsum dolor sit amet, consectetur adipiscing elit, sed do eiusmod tempor incididunt ut labore et dolore magna aliqua. Ut enim ad minim veniam, quis nostrud exercitation</p>
  <div class="footer-name">Harbor Lane Gauging</div>
  <div class="footer-rule-accent"></div>
  <div class="footer-rule"></div>
</section>

<section class="slide content s-two">
  <div class="subtitle">SUB TITLE</div>
  <h2 class="heading">Two Column<span>With Heading</span></h2>
  <div class="lead-box"></div>
  <p class="lead-text">Lorem ipsum dolor sit amet, consectetur adipiscing elit, sed do eiusmod tempor incididunt ut labore et dolore magna aliqua. Ut enim ad minim veniam, quis nostrud exercitation</p>
  <div class="col-head" style="left:127px; top:127px;">Column one heading</div>
  <p class="col-body" style="left:127px; top:152px; width:158px;">Lorem ipsum dolor sit amet, consectetur adipiscing elit, sed do eiusmod tempor incididunt ut labore et dolore magna aliqua. Ut enim ad minim veniam, quis nostrud exercitation</p>
  <div class="col-head" style="left:305px; top:127px;">Column one heading</div>
  <p class="col-body" style="left:305px; top:152px; width:158px;">Lorem ipsum dolor sit amet, consectetur adipiscing elit, sed do eiusmod tempor incididunt ut labore et dolore magna aliqua. Ut enim ad minim veniam, quis nostrud exercitation</p>
  <div class="footer-name">Harbor Lane Gauging</div>
  <div class="footer-rule-accent"></div>
  <div class="footer-rule"></div>
</section>

<section class="slide content s-band">
  <div class="band-photo-warm" role="img" aria-label="Orange-tinted photo of a digital caliper display"></div>
  <div class="band-photo-cool" role="img" aria-label="Navy-tinted photo of a digital caliper with a faint target overlay"></div>
  <div class="band-sub">SUB TITLE</div>
  <h2 class="band-title">Two Column <span>With Heading</span></h2>
  <div class="col-head" style="left:127px; top:135px;">Column one heading</div>
  <p class="col-body" style="left:127px; top:161px; width:330px;">Lorem ipsum dolor sit amet, consectetur adipiscing elit, sed do eiusmod tempor incididunt ut labore et dolore magna aliqua. Ut enim ad minim veniam, quis nostrud exercitation</p>
  <div class="footer-name">Harbor Lane Gauging</div>
  <div class="footer-rule-accent"></div>
  <div class="footer-rule"></div>
</section>

<section class="slide content s-close">
  <div class="close-navy"></div>
  <div class="close-orange"></div>
  <div class="close-name">Harbor Lane<br>Gauging</div>
  <div class="close-url">harborlane<span>gauging</span>.example</div>
</section>

</body>
</html>
```